Linked In Business banner needed

The image size is 1128 px X 191 px

This is a LinkedIn Company Banner. Mora Pell Kite is the company and I have attached our logo. We are an advance staffing company that only recruits sales professionals.

```html
<!DOCTYPE html>
<html lang="en">
<head>
<meta charset="utf-8">
<title>Mora Pell Kite – LinkedIn Company Banner</title>
<link rel="stylesheet" href="https://fonts.googleapis.com/css2?family=Montserrat:ital,wght@0,400;0,700;0,800;1,800&display=swap">
<style>
  :root {
    --page-bg: #f0eef0;
    --navy-deep: #1c3580;
    --navy: #23459f;
    --royal: #2d5cc0;
    --stripe: #1f74d6;
    --stripe-light: #3a8fe8;
    --accent-blue: #3aa0f5;
    --white: #ffffff;
    --photo-warm: #c9b8a4;
    --photo-cool: #9fb3c9;
  }
  * { box-sizing: border-box; margin: 0; padding: 0; }
  html, body {
    width: 1200px;
    height: 1200px;
    overflow: hidden;
    background: var(--page-bg);
    font-family: "Montserrat", Arial, sans-serif;
  }
  .banner-stack {
    position: absolute;
    left: 0;
    top: 267px;
    width: 1200px;
    display: flex;
    flex-direction: column;
    gap: 29px;
  }
  .banner {
    position: relative;
    width: 1200px;
    height: 203px;
    overflow: hidden;
    background:
      radial-gradient(ellipse at 45% 40%, rgba(90,140,230,0.35), transparent 60%),
      linear-gradient(100deg, var(--navy-deep) 0%, var(--navy) 45%, var(--royal) 100%);
  }
  .brand {
    position: absolute;
    left: 36px;
    top: 22px;
    width: 262px;
  }
  .brand-name {
    display: flex;
    align-items: center;
    gap: 10px;
    color: var(--white);
    font-weight: 400;
    font-size: 30px;
    letter-spacing: 0.5px;
    line-height: 1;
  }
  .brand-mark {
    width: 12px;
    height: 12px;
    background: var(--accent-blue);
    flex: none;
  }
  .brand-rule {
    position: absolute;
    left: 2px;
    top: 46px;
    width: 108px;
    height: 1px;
    background: var(--white);
  }
  .brand-tagline {
    position: absolute;
    right: 0;
    top: 40px;
    color: var(--white);
    font-weight: 700;
    font-size: 8.5px;
    letter-spacing: 0.6px;
    white-space: nowrap;
  }
  .headline {
    position: absolute;
    left: 393px;
    top: 30px;
    color: var(--white);
    font-weight: 800;
    font-size: 33px;
    line-height: 36px;
    letter-spacing: 0.3px;
  }
  .subline {
    position: absolute;
    left: 394px;
    top: 142px;
    color: var(--accent-blue);
    font-weight: 800;
    font-style: italic;
    font-size: 15.5px;
    letter-spacing: 1.6px;
  }
  .collage {
    position: absolute;
    left: 0;
    top: 0;
    width: 1200px;
    height: 203px;
  }
</style>
</head>
<body>
<main class="banner-stack">

  <section class="banner">
    <div class="brand">
      <div class="brand-name"><span>Mora Pell Kite</span><span class="brand-mark"></span></div>
      <div class="brand-rule"></div>
      <div class="brand-tagline">YOUR A.I. SALES RECRUITER</div>
    </div>
    <h1 class="headline">SEEKING<br>SALES TEAM PRO<br>SEARCH?</h1>
    <p class="subline">WE RECRUIT HIGH-PERFORMANCE</p>
    <svg class="collage" viewBox="0 0 1200 203" aria-hidden="false">
      <polygon points="760,0 1200,0 1200,203 900,203" fill="var(--stripe)"/>
      <polygon points="1085,0 1200,0 1200,60" fill="var(--stripe-light)" opacity="0.6"/>
      <polygon role="img" aria-label="Photo of two business people shaking hands" points="786,0 952,0 850,62 816,40" fill="var(--photo-warm)"/>
      <polygon role="img" aria-label="Photo of a smiling businessman in a meeting" points="845,99 966,14 1031,133 932,203 900,203" fill="var(--photo-cool)"/>
      <polygon role="img" aria-label="Photo of a team meeting in a bright office" points="962,0 1078,0 1093,25 1008,54" fill="#a7b6c4"/>
      <polygon role="img" aria-label="Photo of a handshake over a signed contract" points="1018,84 1105,31 1152,124 1056,168" fill="#b9c2cc"/>
      <polygon role="img" aria-label="Photo of a businessman shaking hands at a desk" points="1077,155 1161,122 1200,168 1200,203 1096,203" fill="#7f8fa3"/>
    </svg>
  </section>

  <section class="banner">
    <div class="brand">
      <div class="brand-name"><span>Mora Pell Kite</span><span class="brand-mark"></span></div>
      <div class="brand-rule"></div>
      <div class="brand-tagline">YOUR A.I. SALES RECRUITER</div>
    </div>
    <h1 class="headline">SEEKING<br>SALES TEAM PRO<br>SEARCH?</h1>
    <p class="subline">WE RECRUIT HIGH-PERFORMANCE</p>
    <svg class="collage" viewBox="0 0 1200 203" aria-hidden="false">
      <polygon points="760,0 1200,0 1200,203 900,203" fill="var(--stripe)"/>
      <polygon points="1085,0 1200,0 1200,60" fill="var(--stripe-light)" opacity="0.6"/>
      <polygon role="img" aria-label="Photo of two business people shaking hands" points="786,0 952,0 850,62 816,40" fill="var(--photo-warm)"/>
      <polygon role="img" aria-label="Photo of a smiling businessman in a meeting" points="845,99 966,14 1031,133 932,203 900,203" fill="var(--photo-cool)"/>
      <polygon role="img" aria-label="Photo of a team meeting in a bright office" points="962,0 1078,0 1093,25 1008,54" fill="#a7b6c4"/>
      <polygon role="img" aria-label="Photo of a handshake over a signed contract" points="1018,84 1105,31 1152,124 1056,168" fill="#b9c2cc"/>
      <polygon role="img" aria-label="Photo of a businessman shaking hands at a desk" points="1077,155 1161,122 1200,168 1200,203 1096,203" fill="#7f8fa3"/>
    </svg>
  </section>

  <section class="banner">
    <div class="brand">
      <div class="brand-name"><span>Mora Pell Kite</span><span class="brand-mark"></span></div>
      <div class="brand-rule"></div>
      <div class="brand-tagline">YOUR A.I. SALES RECRUITER</div>
    </div>
    <h1 class="headline">SEEKING<br>SALES TEAM PRO<br>SEARCH?</h1>
    <p class="subline">WE RECRUIT HIGH-PERFORMANCE</p>
    <svg class="collage" viewBox="0 0 1200 203" aria-hidden="false">
      <polygon points="760,0 1200,0 1200,203 900,203" fill="var(--stripe)"/>
      <polygon points="1085,0 1200,0 1200,60" fill="var(--stripe-light)" opacity="0.6"/>
      <polygon role="img" aria-label="Photo of two business people shaking hands" points="786,0 952,0 850,62 816,40" fill="var(--photo-warm)"/>
      <polygon role="img" aria-label="Photo of a smiling businessman in a meeting" points="845,99 966,14 1031,133 932,203 900,203" fill="var(--photo-cool)"/>
      <polygon role="img" aria-label="Photo of a team meeting in a bright office" points="962,0 1078,0 1093,25 1008,54" fill="#a7b6c4"/>
      <polygon role="img" aria-label="Photo of a handshake over a signed contract" points="1018,84 1105,31 1152,124 1056,168" fill="#b9c2cc"/>
      <polygon role="img" aria-label="Photo of a businessman shaking hands at a desk" points="1077,155 1161,122 1200,168 1200,203 1096,203" fill="#7f8fa3"/>
    </svg>
  </section>

</main>
</body>
</html>
```